Cafe Menu Required

We need a menu for our coffee shop.
I would like something very much the same as what I have attached.

I have attached a word doc with the items needed on the menu.

I have also attached our logo

I would like to print these on A3 size poster

Industry/Entity Type

Cafe

```html
<!DOCTYPE html>
<html lang="en">
<head>
<meta charset="utf-8">
<title>Brew Hall Canteen — Menu</title>
<link href="https://fonts.googleapis.com/css2?family=Marcellus+SC&display=swap" rel="stylesheet">
<style>
  :root {
    --menu-red: #dc0025;
    --paper: #ffffff;
    --ink-light: #ffffff;
  }
  * { margin: 0; padding: 0; box-sizing: border-box; }
  html, body { width: 1200px; height: 848px; overflow: hidden; background: var(--paper); }
  .menu {
    position: relative;
    width: 1200px;
    height: 848px;
    font-family: "Marcellus SC", "Copperplate", serif;
    background: var(--paper);
  }
  .brand-side {
    position: absolute;
    left: 0; top: 0;
    width: 325px; height: 848px;
    background: var(--paper);
  }
  .brand {
    position: absolute;
    left: 0; top: 108px;
    width: 325px;
    display: flex;
    align-items: center;
    justify-content: center;
    gap: 10px;
    color: var(--menu-red);
    font-size: 34px;
    letter-spacing: 1px;
  }
  .brand-dot {
    width: 18px; height: 18px;
    border-radius: 50%;
    background: var(--menu-red);
  }
  .services {
    position: absolute;
    left: 0; top: 252px;
    width: 318px;
    list-style: none;
    text-align: center;
    color: var(--menu-red);
    font-size: 26px;
    letter-spacing: 0.5px;
  }
  .services li { height: 64.5px; }
  .menu-board {
    position: absolute;
    left: 325px; top: 0;
    width: 875px; height: 848px;
    background: var(--menu-red);
    color: var(--ink-light);
  }
  .section-title {
    position: absolute;
    font-size: 19px;
    font-weight: 400;
    text-decoration: underline;
    text-underline-offset: 3px;
    text-decoration-thickness: 1px;
    letter-spacing: 0.3px;
  }
  .price-list {
    position: absolute;
    list-style: none;
    font-size: 15px;
    letter-spacing: 0.2px;
  }
  .price-list li {
    display: flex;
    justify-content: space-between;
    height: 38.7px;
    white-space: nowrap;
  }
  .hot .section-title { left: 39px; top: 58px; }
  .hot .price-list { left: 39px; top: 99px; width: 355px; }
  .hot .price { width: 118px; }
  .cold .section-title { left: 493px; top: 70px; }
  .cold .price-list { left: 493px; top: 111px; width: 304px; }
  .extras {
    position: absolute;
    left: 478px; top: 508px;
    width: 343px; height: 264px;
    border: 2px solid var(--ink-light);
  }
  .extras .section-title { left: 14px; top: 8px; }
  .extras .price-list { left: 14px; top: 50px; width: 302px; }
  .extras .two-line { height: 46px; align-items: flex-end; line-height: 20px; }
</style>
</head>
<body>
<main class="menu">
  <aside class="brand-side">
    <div class="brand"><span class="brand-dot"></span><span class="brand-name">BREW HALL</span></div>
    <ul class="services">
      <li>• COFFEE •</li>
      <li>• CATERING •</li>
      <li>• FOOD TO GO •</li>
    </ul>
  </aside>

  <section class="menu-board">
    <div class="hot">
      <h2 class="section-title">Hot Beverages</h2>
      <ul class="price-list">
        <li><span>Espresso</span><span class="price">3.5</span></li>
        <li><span>Piccolo</span><span class="price">3.5</span></li>
        <li><span>Short Macchiato</span><span class="price">4.0</span></li>
        <li><span>Long Macchiato</span><span class="price">4.5</span></li>
        <li><span>Latte</span><span class="price">4/4.5/5.5</span></li>
        <li><span>Cappucinno</span><span class="price">4/4.5/5.5</span></li>
        <li><span>Flat White</span><span class="price">4/4.50/5.50</span></li>
        <li><span>Long Black</span><span class="price">4/4.50/5.50</span></li>
        <li><span>Hot Chocolate</span><span class="price">4/4.50/5.50</span></li>
        <li><span>White Hot Chocolate</span><span class="price">4/4.50/5.50</span></li>
        <li><span>Mocha</span><span class="price">4.5/5.0/6.0</span></li>
        <li><span>White Choc Mocha</span><span class="price">4.5/5.0/6.0</span></li>
        <li><span>Chai Latte</span><span class="price">4.5/5.0/6.0</span></li>
        <li><span>Dirty Chai</span><span class="price">5.0/5.5/6.5</span></li>
        <li><span>Selection of Teas</span><span class="price">3.8</span></li>
      </ul>
    </div>

    <div class="cold">
      <h2 class="section-title">Cold Beverages</h2>
      <ul class="price-list">
        <li><span>Iced Latte</span><span>4.5</span></li>
        <li><span>Iced Long Black</span><span>4.5</span></li>
        <li><span>Iced Coffee w/ice cream</span><span>6.0</span></li>
        <li><span>Iced Chocolate w/ice cream</span><span>6.0</span></li>
        <li><span>Coffee Frappe</span><span>6.0</span></li>
        <li><span>Mango Frappe</span><span>6.0</span></li>
      </ul>
    </div>

    <div class="extras">
      <h2 class="section-title">Extras</h2>
      <ul class="price-list">
        <li><span>Extra Shot</span><span>0.5</span></li>
        <li><span>Decaf</span><span>0.5</span></li>
        <li><span>Lactose free</span><span>0.5</span></li>
        <li><span>Soy</span><span>0.5</span></li>
        <li class="two-line"><span>Syrups –<br>Caramel/Hazelnut/Vanilla</span><span>0.5</span></li>
      </ul>
    </div>
  </section>
</main>
</body>
</html>
```